Wageline Associates Business Card Design

We need a business card designed around our new logo. The business card should be modern in design & should communicate success, confidence, power, sophistication. The target market is young business professionals. This is for a human resource & payroll outsourcing business.

```html
<!DOCTYPE html>
<html lang="en">
<head>
<meta charset="UTF-8">
<title>Wageline Associates Business Card</title>
<link rel="stylesheet" href="https://fonts.googleapis.com/css2?family=Roboto:wght@300;400;500&display=swap">
<style>
  :root {
    --brand-red: #ed1c24;
    --ink-black: #050505;
    --text-grey: #444444;
    --card-white: #ffffff;
    --backdrop: #cbcbcb;
  }
  * { margin: 0; padding: 0; box-sizing: border-box; }
  html, body {
    width: 1200px;
    height: 888px;
    overflow: hidden;
    background: var(--backdrop);
    font-family: "Roboto", Arial, sans-serif;
  }
  .business-card {
    position: absolute;
    left: 50px;
    top: 129px;
    width: 1100px;
    height: 630px;
    background: var(--card-white);
    overflow: hidden;
  }
  .brand {
    position: absolute;
    left: 62px;
    top: 285px;
    display: flex;
    align-items: center;
    gap: 14px;
  }
  .brand-dot {
    width: 24px;
    height: 24px;
    border-radius: 50%;
    background: var(--brand-red);
    flex: none;
  }
  .brand-name {
    font-size: 42px;
    font-weight: 500;
    color: var(--ink-black);
    letter-spacing: -0.3px;
    white-space: nowrap;
  }
  .contact-block {
    position: absolute;
    left: 591px;
    top: 140px;
    width: 460px;
  }
  .person-name {
    font-size: 55px;
    font-weight: 500;
    color: var(--brand-red);
    line-height: 1;
    letter-spacing: 0.3px;
  }
  .person-role {
    margin-top: 12px;
    font-size: 26px;
    font-weight: 400;
    color: var(--text-grey);
    text-transform: uppercase;
    line-height: 1;
  }
  .divider {
    width: 380px;
    height: 4px;
    background: var(--brand-red);
  }
  .divider--top { margin-top: 14px; }
  .divider--bottom { margin-top: 14px; }
  .address {
    margin-top: 10px;
    font-size: 29px;
    font-weight: 300;
    color: var(--text-grey);
    line-height: 37px;
    font-style: normal;
  }
  .contact-list {
    list-style: none;
    margin-top: 12px;
  }
  .contact-item {
    display: flex;
    align-items: center;
    gap: 12px;
    font-size: 29px;
    font-weight: 300;
    color: var(--text-grey);
    height: 45px;
  }
  .contact-icon {
    width: 27px;
    height: 27px;
    flex: none;
  }
  .footer-band {
    position: absolute;
    left: 0;
    bottom: 0;
    width: 1100px;
    height: 37px;
  }
</style>
</head>
<body>
  <div class="business-card">
    <div class="brand">
      <span class="brand-dot"></span>
      <span class="brand-name">Wageline Associates</span>
    </div>

    <div class="contact-block">
      <h1 class="person-name">DARA WHITFIELD</h1>
      <p class="person-role">Creative Co-Oppretor</p>
      <div class="divider divider--top"></div>
      <address class="address">1420 Maple Crest Avenue<br>Cedar Hollow, Utah 84120</address>
      <div class="divider divider--bottom"></div>
      <ul class="contact-list">
        <li class="contact-item">
          <svg class="contact-icon" viewBox="0 0 24 24" aria-hidden="true">
            <circle cx="12" cy="12" r="12" fill="var(--brand-red)"/>
            <path d="M8.6 6.5l1.7 2.4-1 1.2c.7 1.5 1.9 2.8 3.5 3.6l1.2-1 2.4 1.6-.8 2c-3.9-.3-7.7-4-8.2-8.2z" fill="#fff"/>
          </svg>
          <span>+000 - 555 - 019</span>
        </li>
        <li class="contact-item">
          <svg class="contact-icon" viewBox="0 0 24 24" aria-hidden="true">
            <circle cx="12" cy="12" r="12" fill="var(--brand-red)"/>
            <rect x="6.5" y="8" width="11" height="8" fill="#fff"/>
            <path d="M6.5 8l5.5 4.5L17.5 8" fill="none" stroke="var(--brand-red)" stroke-width="1.2"/>
          </svg>
          <span>info@wagelinemail.com</span>
        </li>
        <li class="contact-item">
          <svg class="contact-icon" viewBox="0 0 24 24" aria-hidden="true">
            <circle cx="12" cy="12" r="12" fill="var(--brand-red)"/>
            <circle cx="12" cy="12" r="5.5" fill="none" stroke="#fff" stroke-width="1.4"/>
            <ellipse cx="12" cy="12" rx="2.3" ry="5.5" fill="none" stroke="#fff" stroke-width="1.2"/>
            <line x1="6.5" y1="12" x2="17.5" y2="12" stroke="#fff" stroke-width="1.2"/>
          </svg>
          <span>www.wagelineassociates.com</span>
        </li>
      </ul>
    </div>

    <svg class="footer-band" viewBox="0 0 1100 37" preserveAspectRatio="none" aria-hidden="true">
      <polygon points="0,0 555,0 541,37 0,37" fill="var(--ink-black)"/>
      <polygon points="555,0 1100,0 1100,37 541,37" fill="var(--brand-red)"/>
    </svg>
  </div>
</body>
</html>
```